"Cedar Hollow Realty" is the name of my real estate company

This is for a: "for sale" sign, looking for a minimalist design, wire frame outline of a midcentury modern homes roof line or elevation?

My name is: Marcus Dunleavy (needed)
My Cell # is: 415 382 6094 (needed)
My BRE license # is: 02748156 (needed)
BRE needs to be displayed in this format: BRE 02748156 (needed)
The white outline on the sign riders 'pictured" may work on large sign
Note font on pictured rider sign
Updates

This design is for a real estate "for sale" sign or sandwich board sign. Do Not include the words "For Sale" on the sign.

The measurements are 36" inches (91.44 cm) Length, or tall X 24" inches (60.90 cm) Wide.

|
3
---- 24 ----
6
|

Sorry I wasn't more specific earlier. I'd like the elements of the sign to be scaled in size according to their importance, from largest to smallest:

My name: Marcus Dunleavy
My phone number: 415-382-6094
My company name: Cedar Hollow Realty
My license number: BRE 02748156 (This can be much smaller than the smallest text)
Additionally, please incorporate contemporary to mid-century modern elements on the wire frame roofline or a simple roof-like design.

Thank you!

Best regards,
Marcus

```html
<!DOCTYPE html>
<html lang="en">
<head>
<meta charset="utf-8">
<title>Marcus Dunleavy – Yard Sign</title>
<link rel="stylesheet" href="https://fonts.googleapis.com/css2?family=Jost:wght@400;500&display=swap">
<style>
  :root {
    --backdrop: #e8e8e5;
    --sign-black: #131313;
    --sign-white: #ffffff;
  }
  html, body {
    margin: 0;
    padding: 0;
    width: 1200px;
    height: 1123px;
    overflow: hidden;
    background: var(--backdrop);
  }
  .canvas {
    position: relative;
    width: 1200px;
    height: 1123px;
  }
  .yard-sign {
    position: absolute;
    left: 246px;
    top: 30px;
    width: 708px;
    height: 1063px;
    background: var(--sign-black);
    font-family: "Jost", "Helvetica Neue", Arial, sans-serif;
    color: var(--sign-white);
  }
  .sign-frame {
    position: absolute;
    inset: 16px;
    border: 2px solid var(--sign-white);
    box-sizing: border-box;
  }
  .roofline {
    position: absolute;
    left: 104px;
    top: 70px;
    width: 500px;
    height: 170px;
  }
  .roofline path,
  .roofline line {
    fill: none;
    stroke: var(--sign-white);
    stroke-width: 5;
    stroke-linecap: round;
    stroke-linejoin: round;
  }
  .sign-line {
    position: absolute;
    left: 0;
    right: 0;
    margin: 0;
    text-align: center;
    line-height: 1;
    white-space: nowrap;
  }
  .agent-name {
    font-size: 118px;
    font-weight: 500;
    letter-spacing: 1px;
  }
  .agent-name--first { top: 285px; }
  .agent-name--last { top: 420px; }
  .agent-phone {
    top: 600px;
    font-size: 90px;
    font-weight: 500;
  }
  .company-name {
    top: 775px;
    font-size: 40px;
    font-weight: 500;
    letter-spacing: 4px;
  }
  .rule {
    position: absolute;
    left: 254px;
    width: 200px;
    top: 860px;
    height: 2px;
    background: var(--sign-white);
  }
  .agent-license {
    top: 935px;
    font-size: 28px;
    font-weight: 400;
    letter-spacing: 1px;
  }
</style>
</head>
<body>
  <main class="canvas">
    <section class="yard-sign" aria-label="Marcus Dunleavy real estate sign">
      <div class="sign-frame"></div>
      <svg class="roofline" viewBox="0 0 500 170" aria-hidden="true">
        <path d="M10 40 L250 95 L490 15"/>
        <line x1="70" y1="54" x2="70" y2="160"/>
        <line x1="430" y1="35" x2="430" y2="160"/>
        <line x1="250" y1="95" x2="250" y2="160"/>
        <line x1="20" y1="160" x2="480" y2="160"/>
      </svg>
      <p class="sign-line agent-name agent-name--first">MARCUS</p>
      <p class="sign-line agent-name agent-name--last">DUNLEAVY</p>
      <p class="sign-line agent-phone">415 382 6094</p>
      <p class="sign-line company-name">CEDAR HOLLOW REALTY</p>
      <div class="rule"></div>
      <p class="sign-line agent-license">BRE 02748156</p>
    </section>
  </main>
</body>
</html>
```